Plastic Surgeon Needs a business card desing

I need a plastic surgeon business card, Im young , innovative , not afraid of thinking out of the box, What I dont like is human figures or scalpes as designing the card, because I think they are old fashion, I think my name is my strongest card, so I try to find the desing to be something elegant , simple , slick , stylish , radiant with carimsa!

Target Market(s)

PLastics Surgery Patients and doctors to have my data

Industry/Entity Type

Plastic

Contact Information for Business Card

phone numbers need to be legible , right now i have grey scales so they a not to legible

Font styles to use
Serif
Sans Serif

Requirements
Must have
• Personality, and it has to look like a doctor card, not a buisness man card, that is why i think it should be clean , clear , and legible
Nice to have
• Stylilsh, not to heavy card, in means of colors and logos, i think it should give a sensation of health
• Im not sure to have the logo of the hospital i work
Should not have
• human figures
• Hands
• Surgeons

```html
<!DOCTYPE html>
<html lang="es">
<head>
<meta charset="utf-8">
<title>Dr. Martín Olvera – Tarjeta de presentación</title>
<link rel="stylesheet" href="https://fonts.googleapis.com/css2?family=Raleway:wght@400;500&display=swap">
<style>
  :root {
    --backdrop: #0b0b0c;
    --card-top: #4b4c50;
    --card-bottom: #3d3e42;
    --name: #f2f2f2;
    --specialty: #b4b5b8;
    --contact: #e6e6e7;
    --address: #d9d9db;
    --mark-front: #d2d3d5;
    --mark-back: #5e5f63;
  }
  * { margin: 0; padding: 0; box-sizing: border-box; }
  html, body { width: 1200px; height: 900px; overflow: hidden; }
  body {
    background: var(--backdrop);
    font-family: "Raleway", sans-serif;
    position: relative;
  }
  .card {
    position: absolute;
    border-radius: 14px;
    background: linear-gradient(180deg, var(--card-top), var(--card-bottom));
    box-shadow: 0 2px 10px rgba(0,0,0,.5);
    overflow: hidden;
  }
  .card--front { left: 88px; top: 292px; width: 513px; height: 297px; }
  .card--back  { left: 631px; top: 293px; width: 506px; height: 293px; }

  .brand {
    position: absolute;
    left: 38px; top: 112px;
    display: flex; align-items: center; gap: 10px;
    color: var(--mark-front);
    font-weight: 400;
    font-size: 34px;
    letter-spacing: 1px;
  }
  .brand__dot {
    width: 16px; height: 16px; border-radius: 50%;
    background: var(--mark-front);
  }

  .identity { position: absolute; left: 249px; top: 61px; }
  .identity__name { color: var(--name); font-size: 23px; font-weight: 400; line-height: 28px; }
  .identity__specialty { color: var(--specialty); font-size: 15px; line-height: 19px; }

  .contact {
    position: absolute; left: 249px; top: 130px;
    list-style: none;
    color: var(--contact); font-size: 15px; line-height: 19px;
  }

  .address {
    position: absolute; left: 0; right: 24px; top: 244px;
    text-align: center;
    color: var(--address); font-size: 13.5px; line-height: 17px;
  }

  .brand-watermark {
    position: absolute; inset: 0;
    display: flex; align-items: center; justify-content: center;
    color: var(--mark-back);
    font-weight: 400; font-size: 84px; letter-spacing: 3px;
    padding-left: 24px;
  }
</style>
</head>
<body>
  <section class="card card--front">
    <div class="brand"><span class="brand__dot"></span><span>Olvera</span></div>
    <div class="identity">
      <h1 class="identity__name">Dr. Martín Olvera</h1>
      <p class="identity__specialty">Cirugia Plastica</p>
    </div>
    <ul class="contact">
      <li>t: 01 (33) 35207148</li>
      <li>c: 33 3712 6084</li>
      <li>e: martin@drolvera.com</li>
      <li>w: www.drolvera.com</li>
    </ul>
    <p class="address">Av. Robles 2180 Int 45 Torre Médica Central<br>Guadalajara, Jal, México</p>
  </section>

  <section class="card card--back">
    <div class="brand-watermark">Olvera</div>
  </section>
</body>
</html>
```